Dermavale "polish what the seasons left you" The whole body approach to beauty, customized skincare a

I need a stronger logo design than what I have now. I currently have a small med spa in Ashmere, IL. I will be expanding my brand to Vellport City and the Dunholt of NY. The services I provide in Ashmere include; advanced medical grade skincare treatments, laser, plastic surgery and nutrition counsel. My concept is personalized skincare. Part of my philosophy is to dedicate a lot of time and make myself always available to my clients questions and concerns. To maintain integrity of the Dermavale Philosophy I do not advertise. Dermavale is an "exclusive skincare club" therefore you must be referred by an existing client or staff member in order to get an appointment. My Ashmere clientele consists of young professionals competing with their peers to look their absolute best. The Vellport and Dunholt business has a completely different structure. It is a Mobile med spa service providing treatments at people's homes. The services provided are advanced skincare, wellness, massage, spray tan, hair and makeup. My vision for the new logo design is to exude an image that is both cutting edge, relevant, sophisticated, sexy and modern (sleek) yet practical and strong. It must be eye catching yet simplistic, aesthetically pleasing to look at and above all must promote EXCLUSIVITY! bellow I have attached my current logo design which is printed using silver and gold foil. The other is the logo on my prescription skincare products. I need to merge the two for the brand to be cohesive. I would like to print my business cards on a mirror like material where you can see your reflection. Front of card: the brand Dermavale across the front and across the bottom will be Ashmere. Vellport. Dunholt Back of card: in a font style like writing "Dermavale is the whole body approach to beauty. customized medical grade skincare. massage. wellness counsel. By appointment only
www.dermavalewellness-example.com p: (555) 318-2406
I am open to all suggestions to make my brand as strong as possible. Please be creative and relevant. Thank you!

```html
<!DOCTYPE html>
<html lang="en">
<head>
<meta charset="utf-8">
<title>Dermavale Business Card</title>
<link rel="stylesheet" href="https://fonts.googleapis.com/css2?family=Montserrat:wght@300&family=Julius+Sans+One&family=Poiret+One&display=swap">
<style>
  :root {
    --backdrop: #3c3c3c;
    --card: #ffffff;
    --ink: #8c8c8c;
    --ink-soft: #a0a0a0;
  }
  * { margin: 0; padding: 0; box-sizing: border-box; }
  html, body {
    width: 1031px;
    height: 1200px;
    overflow: hidden;
    background: var(--backdrop);
  }
  .canvas {
    position: relative;
    width: 1031px;
    height: 1200px;
    background: var(--backdrop);
  }
  .card {
    position: absolute;
    left: 92px;
    width: 852px;
    background: var(--card);
  }
  .card--front { top: 67px; height: 472px; }
  .card--back { top: 662px; height: 470px; }

  .brand {
    position: absolute;
    left: 317px;
    width: 476px;
    top: 298px;
    font-family: "Montserrat", sans-serif;
    font-weight: 300;
    font-size: 74px;
    letter-spacing: 2px;
    line-height: 1;
    color: var(--ink);
    white-space: nowrap;
  }
  .locations {
    position: absolute;
    left: 319px;
    width: 474px;
    top: 395px;
    display: flex;
    justify-content: space-between;
    font-family: "Montserrat", sans-serif;
    font-weight: 300;
    font-size: 20px;
    letter-spacing: 1.5px;
    color: var(--ink-soft);
    white-space: nowrap;
  }

  .tagline {
    position: absolute;
    left: 0;
    right: 0;
    top: 98px;
    text-align: center;
    font-family: "Julius Sans One", sans-serif;
    font-size: 30px;
    color: var(--ink);
    white-space: nowrap;
  }
  .services {
    position: absolute;
    left: 0;
    right: 0;
    top: 180px;
    list-style: none;
    text-align: center;
    font-family: "Poiret One", sans-serif;
    font-size: 25px;
    line-height: 48px;
    color: var(--ink);
  }
  .services li span { margin: 0 16px; }

  .contact {
    position: absolute;
    top: 412px;
    font-family: "Montserrat", sans-serif;
    font-weight: 300;
    font-size: 19px;
    color: var(--ink);
    white-space: nowrap;
  }
  .contact--web { left: 77px; }
  .contact--phone { right: 78px; }
</style>
</head>
<body>
<main class="canvas">
  <section class="card card--front" aria-label="Card front">
    <div class="brand">DERMAVALE</div>
    <div class="locations"><span>ASHMERE</span><span>|</span><span>VELLPORT</span><span>|</span><span>DUNHOLT</span></div>
  </section>

  <section class="card card--back" aria-label="Card back">
    <p class="tagline">POLISH WHAT THE SEASONS LEFT YOU...</p>
    <ul class="services">
      <li><span>CUSTOMIZED CLINICAL SKINCARE</span><span>FACIAL REJUVENATION</span></li>
      <li><span>NUTRITION ANALYSIS</span><span>ACNE THERAPY</span></li>
      <li><span>WELLNESS COUNSEL</span><span>MASSAGE</span></li>
    </ul>
    <p class="contact contact--web">www.dermavalewellness-example.com</p>
    <p class="contact contact--phone">p: (555) 318-2406</p>
  </section>
</main>
</body>
</html>
```